Fire Alarm and Access Control Permit Drawings

My company engineers and designs fire alarm and access control drawings for companies that install these type systems in commercial office buildings. We want a post card mailer to go out to all fire alarm and security companies in Texas. We want companies to outsource their fire alarm and access control drawings to us. We do submittal, as-built and permit drawings specific to the security and fire alarm industry. Our price list is on the web site at www.kvrplanworks.com/pricelist.html.
Here is a good example of words to use:
"KVR Plan Works specializes in submittal, as-built and permit drawings for the commercial fire alarm and access control industry. We prepare and submit plans on your behalf to jurisdictions and consultants all over Texas. Give us a call today!"

Target Market(s)

Commercial fire alarm and security integrators who currently do their drawings in-house or through a 3rd party like us.

Industry/Entity Type

Security

Requirements
Must have
• Must have front and back side with room for addressing, must have our web address, physical address and phone number. State on the post card to contact Owen Tulley for more information or questions.

www.kvrplanworks.com

7218 Brackenford Street
Suite 342
Houston, Texas 77413
Nice to have
• We like the look and feel of building floor plans on a desk or rolled up with drafting tools. But we do not want to convey that we hand-draw our plans. Everything we do is drawn in AutoCAD.
Nice to have a link to our web site or reference to the pricelist being on the web site. www.kvrplanworks.com/pricelist.html.
Should not have
• Don't be too wordy.

```html
<!DOCTYPE html>
<html lang="en">
<head>
<meta charset="utf-8">
<title>KVR Plan Works – Postcard Mailer</title>
<link rel="stylesheet" href="https://fonts.googleapis.com/css2?family=Libre+Baskerville:wght@700&family=Roboto+Condensed:wght@300;400&family=Special+Elite&display=swap">
<style>
  :root {
    --navy: #242a5c;
    --blue: #3b6fb6;
    --yellow: #f6e500;
    --steel-light: #d3dbe3;
    --steel-dark: #7d8d9c;
    --paper: #ffffff;
    --ink: #2f3033;
    --title-ink: #5a5a5a;
    --line: #3a3a3a;
    --backdrop: #ebe8e3;
  }
  * { box-sizing: border-box; margin: 0; padding: 0; }
  html, body { width: 806px; height: 1200px; overflow: hidden; }
  body { background: var(--backdrop); position: relative; font-family: "Roboto Condensed", sans-serif; }

  .card { position: absolute; left: 77px; width: 650px; overflow: hidden; box-shadow: 0 3px 10px rgba(0,0,0,.25); }
  .card svg.shapes { position: absolute; inset: 0; }

  /* Front */
  .card--front { top: 63px; height: 510px; }
  .brand-name {
    position: absolute; left: 24px; top: 40px;
    font-family: "Roboto Condensed", sans-serif; font-weight: 400;
    font-size: 30px; letter-spacing: 1px; color: var(--paper);
  }
  .front-title {
    position: absolute; left: 311px; top: 282px; width: 240px;
    font-family: "Special Elite", monospace; font-size: 25px; line-height: 36px;
    color: var(--title-ink); letter-spacing: .5px;
  }

  /* Back */
  .card--back { top: 617px; height: 506px; background: var(--paper); }
  .who-title {
    position: absolute; left: 23px; top: 157px;
    font-family: "Libre Baskerville", serif; font-weight: 700; font-size: 20px; color: var(--navy);
  }
  .who-copy {
    position: absolute; left: 23px; top: 198px; width: 292px;
    font-weight: 300; font-size: 15.4px; line-height: 22px; color: var(--ink);
  }
  .who-copy p + p { margin-top: 22px; }
  .contact { position: absolute; left: 16px; top: 392px; color: var(--paper); font-size: 10px; line-height: 11px; }
  .contact__name { font-size: 19px; color: var(--yellow); margin: 0 0 5px 15px; line-height: 22px; }
  .contact__row { display: flex; align-items: flex-start; gap: 4px; margin-bottom: 5px; }
  .contact__row svg { flex: none; margin-top: 1px; }
  .stamp-box { position: absolute; left: 547px; top: 83px; width: 71px; height: 71px; border: 1.5px solid var(--line); }
  .address-line { position: absolute; left: 361px; width: 273px; border-top: 1px solid var(--line); }
</style>
</head>
<body>

<section class="card card--front">
  <svg class="shapes" width="650" height="510" viewBox="0 0 650 510">
    <defs>
      <linearGradient id="steel" x1="0" y1="0" x2="1" y2="1">
        <stop offset="0" stop-color="var(--steel-light)"/>
        <stop offset="1" stop-color="var(--steel-dark)"/>
      </linearGradient>
      <linearGradient id="band" x1="0" y1="0" x2="1" y2="0">
        <stop offset="0" stop-color="var(--navy)"/>
        <stop offset=".55" stop-color="var(--navy)"/>
        <stop offset="1" stop-color="var(--blue)"/>
      </linearGradient>
    </defs>
    <rect width="650" height="510" fill="url(#steel)" role="img" aria-label="Photo of rolled building floor plans, drafting compass and pencil beside a keyboard"/>
    <polygon points="0,0 365,0 0,285" fill="var(--navy)"/>
    <polygon points="0,218 60,175 22,272" fill="var(--blue)"/>
    <polygon points="365,0 372,0 28,272 20,276" fill="var(--yellow)"/>
    <polygon points="300,40 362,5 40,262 22,272" fill="var(--yellow)"/>
    <polygon points="292,276 300,276 300,414 540,414 536,424 292,424" fill="var(--navy)"/>
    <polygon points="300,260 545,260 558,274 650,214 650,465 528,465 546,404 300,404" fill="var(--yellow)"/>
    <polygon points="86,465 650,465 650,510 72,510" fill="url(#band)"/>
  </svg>
  <div class="brand-name">KVR Plan Works</div>
  <h1 class="front-title">Fire Alarm and Access Control Drawings</h1>
</section>

<section class="card card--back">
  <svg class="shapes" width="650" height="506" viewBox="0 0 650 506">
    <defs>
      <linearGradient id="photo-back" x1="0" y1="0" x2="1" y2="1">
        <stop offset="0" stop-color="#c9c9c9"/>
        <stop offset="1" stop-color="#7e7e7e"/>
      </linearGradient>
      <linearGradient id="contact-band" x1="0" y1="0" x2="1" y2="0">
        <stop offset="0" stop-color="var(--navy)"/>
        <stop offset="1" stop-color="var(--blue)"/>
      </linearGradient>
    </defs>
    <polygon points="10,28 212,192 316,92 316,0 10,0" fill="var(--navy)"/>
    <polygon points="4,0 212,175 316,72 316,0" fill="var(--yellow)"/>
    <polygon points="40,0 212,160 316,58 316,0" fill="url(#photo-back)" role="img" aria-label="Photo of rolled blueprints stacked together"/>
    <polygon points="70,372 300,400 306,430 150,415" fill="var(--yellow)"/>
    <polygon points="0,362 70,372 150,415 313,430 313,506 0,506" fill="url(#contact-band)"/>
  </svg>

  <h2 class="who-title">Who We Are</h2>
  <div class="who-copy">
    <p>KVR Plan Works specializes in submittal, as-built and permit drawings for the commercial fire alarm and access control industry. We prepare and submit plans on your behalf to jurisdictions and consultants all over Texas.</p>
    <p>Give us a call today!</p>
  </div>

  <div class="contact">
    <p class="contact__name">Owen Tulley</p>
    <div class="contact__row">
      <svg width="8" height="10" viewBox="0 0 8 10"><path d="M4 0a4 4 0 0 1 4 4c0 3-4 6-4 6S0 7 0 4a4 4 0 0 1 4-4z" fill="#fff"/><circle cx="4" cy="4" r="1.5" fill="var(--navy)"/></svg>
      <span>7218 Brackenford Street<br>Suite 342<br>Houston, Texas 77413</span>
    </div>
    <div class="contact__row">
      <svg width="9" height="9" viewBox="0 0 10 10"><circle cx="5" cy="5" r="4.5" fill="#d9d9d9"/><path d="M.5 5h9M5 .5c-2 2.5-2 6.5 0 9M5 .5c2 2.5 2 6.5 0 9" stroke="var(--navy)" stroke-width=".6" fill="none"/></svg>
      <span>www.kvrplanworks.com</span>
    </div>
    <div class="contact__row">
      <svg width="9" height="9" viewBox="0 0 10 10"><circle cx="5" cy="5" r="4.5" fill="#d9d9d9"/><path d="M.5 5h9M5 .5c-2 2.5-2 6.5 0 9M5 .5c2 2.5 2 6.5 0 9" stroke="var(--navy)" stroke-width=".6" fill="none"/></svg>
      <span>www.kvrplanworks.com/pricelist.html</span>
    </div>
  </div>

  <div class="stamp-box"></div>
  <div class="address-line" style="top:243px"></div>
  <div class="address-line" style="top:283px"></div>
  <div class="address-line" style="top:321px"></div>
</section>

</body>
</html>
```